Business Card & Stationary Design Project

We are looking for some creative direction for business cards and our stationary.

We are a global logistics firm that has recently changed its name to Marrick Global Logistics and we have a new website due out tomorrow (www.marrick.com.au).

The colours of the company are rich navy tones, I would like to have business cards that fit together to make one picture on the back (possibly an old map of the world??), and the front to be modern contemporary looking.

But I am open to suggestions, so just incorporate our new logo and get going!
Updates

Hi Everyone,

Thank you for all of your designs so far and the time you have put into it.

I have asked many of you for amendments to see if we can get a final product, so with this in mind I am extending the deadline by a few days.

Good luck and thank you once again.

Please message me direct if you need any clarification.

Kind Regards
Colin

Reason: As outlined the extra 3 days is for amendments and changes to the current submissions. Thanks Colin

Industry/Entity Type

Business

```html
<!DOCTYPE html>
<html lang="en">
<head>
<meta charset="utf-8">
<title>Marrick Global Logistics – Stationery Set</title>
<link rel="stylesheet" href="https://fonts.googleapis.com/css2?family=Source+Sans+3:wght@400;600&display=swap">
<style>
  :root {
    --navy: #1d3a78;
    --navy-deep: #142c62;
    --blue: #2f5fb0;
    --sky: #a9d4f0;
    --pale: #e6f0fa;
    --ink: #1f2f6a;
    --paper: #ffffff;
    --table: #e9ebef;
    --font: "Source Sans 3", "Myriad Pro", Arial, sans-serif;
  }
  * { box-sizing: border-box; margin: 0; padding: 0; }
  html, body { width: 1200px; height: 900px; overflow: hidden; }
  body { background: var(--table); font-family: var(--font); color: var(--ink); position: relative; }

  .sheet { position: absolute; background: var(--paper); overflow: hidden; box-shadow: 0 2px 8px rgba(0,0,0,.18); }
  .sheet > svg { position: absolute; left: 0; top: 0; }

  .letterhead { left: 25px; top: 28px; width: 660px; height: 853px; }
  .card-front { left: 612px; top: 225px; width: 310px; height: 178px; }
  .card-back { left: 866px; top: 28px; width: 334px; height: 178px; background: linear-gradient(135deg, #2a5cab, var(--navy) 70%); }
  .envelope { left: 470px; top: 420px; width: 730px; height: 440px; background: none; box-shadow: none; overflow: visible; }

  .brand { position: absolute; display: flex; align-items: center; gap: 12px; }
  .brand-name { color: var(--ink); font-weight: 400; line-height: 1; }
  .brand-name .word { display: block; letter-spacing: .22em; }
  .brand-name .sub { display: block; letter-spacing: .3em; }
  .brand-dot { border-radius: 50%; background: var(--blue); flex: none; }

  .letterhead .brand { left: 28px; top: 82px; }
  .letterhead .word { font-size: 36px; }
  .letterhead .sub { font-size: 10.5px; margin-top: 2px; }
  .letterhead .brand-dot { width: 80px; height: 80px; }

  .card-front .brand { left: 10px; top: 34px; gap: 6px; }
  .card-front .word { font-size: 16px; }
  .card-front .sub { font-size: 5px; margin-top: 1px; }
  .card-front .brand-dot { width: 36px; height: 36px; }

  .envelope .brand { left: 18px; top: 188px; gap: 10px; }
  .envelope .word { font-size: 26px; }
  .envelope .sub { font-size: 8px; margin-top: 2px; }
  .envelope .brand-dot { width: 64px; height: 64px; }

  .contact { position: absolute; list-style: none; color: var(--ink); }
  .contact li { display: flex; align-items: center; gap: 4px; }
  .contact svg { flex: none; }
  .letterhead .contact { left: 28px; top: 740px; font-size: 11px; line-height: 13px; }
  .card-front .contact { left: 188px; top: 76px; font-size: 8px; line-height: 10.3px; }

  .address { position: absolute; color: var(--ink); }
  .letterhead .address { left: 28px; top: 800px; font-size: 11px; line-height: 13px; }
  .card-front .address { left: 188px; top: 137px; font-size: 8px; line-height: 10.5px; }

  .holder { position: absolute; right: 22px; top: 16px; text-align: right; color: #fff; }
  .holder-name { font-size: 14px; font-weight: 400; }
  .holder-title { font-size: 9px; margin-right: 20px; }

  .map-area { position: absolute; }
  .card-front .map-area { left: 0; top: 88px; width: 175px; height: 90px;
    background: radial-gradient(ellipse at 45% 70%, #c6ddf2, rgba(214,230,246,.4) 60%, rgba(255,255,255,0) 80%); }
  .letterhead .map-area.faint { left: 250px; top: 460px; width: 410px; height: 393px;
    background: radial-gradient(ellipse at 65% 55%, #dfe9f6, rgba(232,240,250,.5) 55%, rgba(255,255,255,0) 75%); }
  .card-back .map-area { inset: 0; background: radial-gradient(ellipse at 45% 45%, rgba(110,160,220,.45), rgba(110,160,220,0) 65%); }

  .card-back .url { position: absolute; left: 20px; bottom: 16px; color: #fff; font-size: 16px; letter-spacing: .04em; }

  .return-address { position: absolute; left: 225px; top: 106px; font-size: 11px; color: var(--navy-deep); transform: rotate(180deg); white-space: nowrap; }
</style>
</head>
<body>

<!-- Letterhead -->
<section class="sheet letterhead">
  <svg width="660" height="853" viewBox="0 0 660 853">
    <defs>
      <clipPath id="lh-clip"><path d="M0,0 H660 V128 C600,160 520,172 440,152 C340,125 250,48 0,40 Z"/></clipPath>
      <radialGradient id="lh-map" cx="0.55" cy="0.3" r="0.6">
        <stop offset="0" stop-color="#3b6fbd"/><stop offset="1" stop-color="#1d3a78" stop-opacity="0"/>
      </radialGradient>
    </defs>
    <path d="M0,40 C250,48 340,125 440,152 C520,172 600,160 660,128 V136 C600,172 520,184 440,164 C330,136 250,72 0,70 Z" fill="var(--sky)"/>
    <path d="M0,0 H660 V128 C600,160 520,172 440,152 C340,125 250,48 0,40 Z" fill="var(--navy)"/>
    <g clip-path="url(#lh-clip)"><rect x="250" y="0" width="410" height="180" fill="url(#lh-map)"/></g>
  </svg>
  <div class="map-area faint" role="img" aria-label="Faint world map decoration"></div>
  <div class="brand">
    <span class="brand-name"><span class="word">MARRICK</span><span class="sub">Global Logistics</span></span>
    <span class="brand-dot"></span>
  </div>
  <ul class="contact">
    <li><svg width="9" height="9" viewBox="0 0 10 10"><path d="M2,1 L4,1 L4.5,3 L3.3,4 C4,5.5 4.5,6 6,6.7 L7,5.5 L9,6 L9,8 C5,9 1,5 2,1Z" fill="var(--blue)"/></svg>02 9146 2200</li>
    <li><svg width="9" height="9" viewBox="0 0 10 10"><rect x="2.5" y="0.5" width="5" height="9" rx="1" fill="var(--blue)"/></svg>0400517382</li>
    <li><svg width="9" height="9" viewBox="0 0 10 10"><rect x="1" y="3" width="8" height="6" rx="1" fill="var(--blue)"/><rect x="3" y="1" width="4" height="3" fill="var(--blue)"/></svg>029146 2299</li>
    <li><svg width="9" height="9" viewBox="0 0 10 10"><circle cx="5" cy="5" r="4" fill="none" stroke="var(--blue)"/><path d="M1,5 H9 M5,1 V9" stroke="var(--blue)"/></svg>marrick.com.au</li>
  </ul>
  <p class="address">58 Harbour Lane<br>Eastbrook NSW 2050</p>
</section>

<!-- Business card back -->
<section class="sheet card-back">
  <div class="map-area" role="img" aria-label="World map illustration in blue tones"></div>
  <p class="url">MARRICK.COM.AU</p>
</section>

<!-- Business card front -->
<section class="sheet card-front">
  <svg width="310" height="178" viewBox="0 0 310 178">
    <path d="M0,10 C80,10 140,34 190,52 C240,68 280,66 310,52 V58 C280,74 240,76 190,60 C140,44 80,22 0,22 Z" fill="var(--sky)"/>
    <path d="M0,0 H310 V52 C280,66 240,68 190,52 C140,34 80,10 0,10 Z" fill="var(--navy)"/>
  </svg>
  <div class="holder">
    <p class="holder-name">Your Name Here</p>
    <p class="holder-title">Your Title Here</p>
  </div>
  <div class="brand">
    <span class="brand-name"><span class="word">MARRICK</span><span class="sub">Global Logistics</span></span>
    <span class="brand-dot"></span>
  </div>
  <div class="map-area" role="img" aria-label="Faint world map decoration"></div>
  <ul class="contact">
    <li><svg width="7" height="7" viewBox="0 0 10 10"><path d="M2,1 L4,1 L4.5,3 L3.3,4 C4,5.5 4.5,6 6,6.7 L7,5.5 L9,6 L9,8 C5,9 1,5 2,1Z" fill="var(--blue)"/></svg>02 9146 2200</li>
    <li><svg width="7" height="7" viewBox="0 0 10 10"><rect x="2.5" y="0.5" width="5" height="9" rx="1" fill="var(--blue)"/></svg>0400517382</li>
    <li><svg width="7" height="7" viewBox="0 0 10 10"><rect x="1" y="3" width="8" height="6" rx="1" fill="var(--blue)"/><rect x="3" y="1" width="4" height="3" fill="var(--blue)"/></svg>029146 2299</li>
    <li><svg width="7" height="7" viewBox="0 0 10 10"><rect x="0.5" y="2" width="9" height="6" rx="1" fill="var(--blue)"/></svg>colin@marrick.com.au</li>
    <li><svg width="7" height="7" viewBox="0 0 10 10"><circle cx="5" cy="5" r="4" fill="none" stroke="var(--blue)"/><path d="M1,5 H9 M5,1 V9" stroke="var(--blue)"/></svg>marrick.com.au</li>
  </ul>
  <p class="address">58 Harbour Lane<br>Eastbrook NSW 2050</p>
</section>

<!-- Envelope -->
<section class="sheet envelope">
  <svg width="730" height="440" viewBox="0 0 730 440">
    <defs>
      <clipPath id="env-clip"><path d="M8,85 C150,40 340,2 440,2 H700 C722,30 730,70 730,140 V238 C680,254 600,254 540,238 C430,208 330,152 0,160 V90 Z"/></clipPath>
      <radialGradient id="env-map" cx="0.75" cy="0.45" r="0.5">
        <stop offset="0" stop-color="#3b6fbd"/><stop offset="1" stop-color="#1d3a78" stop-opacity="0"/>
      </radialGradient>
    </defs>
    <rect x="0" y="85" width="730" height="355" fill="var(--paper)"/>
    <path d="M0,160 C330,152 430,208 540,238 C600,254 680,254 730,238 V246 C680,264 600,264 540,248 C430,220 330,168 0,178 Z" fill="var(--sky)"/>
    <path d="M8,85 C150,40 340,2 440,2 H700 C722,30 730,70 730,140 V238 C680,254 600,254 540,238 C430,208 330,152 0,160 V90 Z" fill="var(--navy)"/>
    <g clip-path="url(#env-clip)"><rect x="380" y="0" width="350" height="260" fill="url(#env-map)" role="img" aria-label="World map illustration"/></g>
  </svg>
  <p class="return-address">58 Harbour Lane Eastbrook NSW 2050</p>
  <div class="brand">
    <span class="brand-name"><span class="word">MARRICK</span><span class="sub">Global Logistics</span></span>
    <span class="brand-dot"></span>
  </div>
</section>

</body>
</html>
```